Post card design for ( Interior ) & ( Exterior ) Residential Painting

We need a post card design for interior painting. To get homeowners to call about getting there interior home painted before the end winter comes, to get a clean, quality and no hassle paint job with low odor paints

Some IDEAS:
Exterior Paint Season is Coming to Northern VA and Metro DC!
Have you taken a look around your house this winter? Have you noticed any areas of unwanted moisture, mold or draft? Keeping your house painted and well-maintained on the outside will save money in the future as well. It protects your home from the elements – whether, wind, rain and snow or the strong summer sun.

idea #2
Exterior Paint Makes Your House Last Longer
aintaining a good coat of the correct type of paint on the exterior of your home will help protect your home from the elements and extend the overall life of the structure
idea #3
Rotten Wood and Two Other TOP Reasons for Exterior Paint
We’ll start there – rotten wood – the first reason for exterior paint. If your home or building has decorative wood trim, wood siding or even wood around windows and doors, it could be at risk for rotten or rotting wood. Maintaining a healthy and COMPLETE coat of paint will protect the wood from water damage. Additionally, during a paint project, our team can assess wooden areas and advise if there are any places of concern. For a long-term solution, consider replacing wood trim with vinyl or wood alternatives that stand up to the elements. This can also be done during an exterior paint project.
Idea # 4
Benefits of Using Low-VOC interior Paints
Paints with low-VOC or Zero-VOC are considered healthier options due to the lower amount of toxins they release when applied to a wall. Latex paints are popular low-VOC because they are water based and don’t contain other chemicals you may find in oil-based paints.

Less odor! Because these paints have lower levels of toxins that are released, the paint smell that is associated with a fresh coat of paint is not as strong. Low-VOC would be a great option if you plan on painting a nursery because the smell won’t linger. Although you might not smell it, it is always important to ventilate the room. All paints, even low-VOC have levels of toxicity which are not good to breathe in for long periods of time.

Target Market(s)

single family homes

Colors

Designer to choose colors to be used in the design.

Requirements
Should not have
• cheep, free

```html
<!DOCTYPE html>
<html lang="en">
<head>
<meta charset="utf-8">
<title>Brightline Painting – Exterior Season Postcard</title>
<link rel="stylesheet" href="https://fonts.googleapis.com/css2?family=Oswald:wght@500;600;700&family=Lato:wght@400;700;900&family=Roboto:wght@500;700&display=swap">
<style>
:root{
  --red:#e21d3c;
  --red-dark:#8e1520;
  --ink:#1f1d1e;
  --white:#ffffff;
  --bg:#d9d9dc;
  --rule:#c9c9c9;
  --photo-sky:#9fb3c8;
  --photo-brick:#7d5a55;
  --photo-stone:#b9bcc0;
}
*{box-sizing:border-box;margin:0;padding:0}
html,body{width:1200px;height:1200px;overflow:hidden;background:var(--bg)}
body{position:relative;font-family:"Lato",sans-serif;color:var(--ink)}
.card{position:absolute;left:203px;width:794px;height:540px;background:var(--white);overflow:hidden}
.card--front{top:46px}
.card--back{top:611px}
.abs{position:absolute}

/* brand name block */
.brand{position:absolute;display:flex;align-items:center;gap:10px}
.brand__mark{width:14px;height:14px;background:var(--red)}
.brand__name{font-family:"Oswald",sans-serif;font-weight:700;color:var(--ink);text-transform:uppercase;line-height:.95}
.card--front .brand{left:37px;top:122px}
.card--front .brand__name{font-size:40px}
.card--back .brand{left:485px;top:58px}
.card--back .brand__name{font-size:24px}

/* front */
.hero-art{position:absolute;left:0;top:0}
.headline{left:39px;top:250px;width:340px;font-family:"Oswald",sans-serif;font-weight:600;font-size:37px;line-height:42px;text-transform:uppercase;color:var(--ink);letter-spacing:-1px;white-space:nowrap}
.headline .accent{color:var(--red)}
.lead-title{left:42px;top:426px;font-family:"Roboto",sans-serif;font-weight:700;font-size:19px;color:var(--red)}
.lead-body{left:42px;top:456px;width:715px;font-size:13.4px;line-height:17px;color:var(--ink)}
.rules{position:absolute;left:0;width:100%}
.rules span{position:absolute;left:0;width:100%;height:2px;background:var(--red)}

/* back */
.why-panel{left:0;top:0;width:435px;height:362px;background:var(--red)}
.why-title{left:30px;top:20px;font-weight:700;font-size:34px;color:var(--white)}
.why-list{left:36px;top:62px;list-style:none;color:var(--white);font-size:9.2px;line-height:14.1px}
.why-list li{position:relative;padding-left:11px}
.why-list li::before{content:"";position:absolute;left:0;top:3.5px;border-left:6px solid var(--white);border-top:3.5px solid transparent;border-bottom:3.5px solid transparent}
.gallery{left:16px;top:213px;width:405px;height:141px;background:var(--ink);padding:2px;display:flex;gap:2px}
.gallery__photo{position:relative;flex:1}
.gallery__tag{position:absolute;font-size:7px;font-weight:700;color:var(--white)}
.about-band{left:0;top:362px;width:435px;height:88px;background:var(--ink)}
.about-text{left:30px;top:369px;width:190px;font-size:7.6px;line-height:10.5px;color:var(--white)}
.call-label{left:231px;top:381px;width:190px;text-align:center;font-family:"Oswald",sans-serif;font-weight:600;font-size:17px;letter-spacing:1px;color:var(--red);text-transform:uppercase}
.call-number{left:231px;top:400px;width:190px;text-align:center;font-weight:900;font-size:27px;color:var(--white)}
.stamp-box{left:676px;top:35px;width:85px;height:106px;border:1px solid var(--rule)}
.address-line{left:485px;width:275px;height:1px;background:var(--rule)}
.areas-title{left:458px;top:397px;width:299px;text-align:center;font-weight:700;font-size:11px;color:var(--red);text-decoration:underline}
.areas-text{left:458px;top:415px;width:299px;text-align:center;font-size:7.3px;line-height:10.5px;color:var(--ink)}
.contact-bar{left:0;top:450px;width:794px;height:52px;background:var(--red)}
.contact{position:absolute;top:460px;display:flex;align-items:center;gap:7px;color:var(--white);font-size:10.8px;line-height:14px}
.contact--addr{left:30px}
.contact--phone{left:252px}
.contact--web{left:372px}
.badge{position:absolute;top:460px;height:31px;background:var(--white);border-radius:2px}
.footer-left{left:0;top:502px;width:435px;height:38px;background:var(--ink)}
</style>
</head>
<body>

<!-- FRONT -->
<section class="card card--front" aria-label="Postcard front">
  <svg class="hero-art" width="794" height="540" viewBox="0 0 794 540">
    <polygon points="171,0 245,0 545,417" fill="var(--red-dark)"/>
    <polygon points="245,0 313,0 545,417" fill="var(--red)"/>
    <polygon points="313,0 794,0 794,194 545,417" fill="var(--photo-stone)" role="img" aria-label="Photo of a row of Victorian brick and stone townhouses framed by green trees"/>
    <polygon points="406,302 472,342 545,417 432,380" fill="var(--ink)"/>
    <polygon points="405,414 461,390 545,417" fill="var(--red-dark)"/>
    <polygon points="794,194 794,306 545,417" fill="var(--red)"/>
  </svg>

  <div class="brand">
    <span class="brand__mark"></span>
    <div class="brand__name">Brightline<br>Painting</div>
  </div>

  <h1 class="abs headline"><span class="accent">Exterior Paint</span> Season<br>is coming to Northern<br><span class="accent">VA and Metro DC!</span></h1>

  <h2 class="abs lead-title">Have you taken a look around your house this winter?</h2>
  <p class="abs lead-body">Have you noticed any areas of unwanted moisture, mold or draft? Keeping your house painted and well-maintained on the outside will save money in the future as well. It protects your home from the elements – whether, wind, rain and snow or the strong summer sun.</p>

  <div class="rules" style="top:509px">
    <span style="top:0"></span><span style="top:10px"></span><span style="top:20px"></span>
  </div>
</section>

<!-- BACK -->
<section class="card card--back" aria-label="Postcard back">
  <div class="abs why-panel"></div>
  <h2 class="abs why-title">Why us?</h2>
  <ul class="abs why-list">
    <li>Affordable written quotes – interior and exterior</li>
    <li>Residential Painters- houses, condos, townhouse, apartments</li>
    <li>Commercial Painters- HOAs, churches, hotels, retailers, offices and industrial buildings</li>
    <li>Deal with local owners</li>
    <li>Two-year guarantee with written warranty – Click for Warranty PDF</li>
    <li>Color matching and color consultation expert advice</li>
    <li>High-quality paint brands – custom formulations</li>
    <li>Professional credentials- TRB A+ rating, Painters Guild, Riverside Chamber</li>
    <li>Secondary services- carpentry, drywall, plaster, wallpaper, power wash</li>
    <li>Licensed &amp; Insured painters in VA, MD, DC</li>
  </ul>

  <div class="abs gallery">
    <div class="gallery__photo" role="img" aria-label="Before photo of a faded grey house wall" style="background:linear-gradient(#c9ccd0,#8d9398)"><span class="gallery__tag" style="left:20px;top:5px">Before</span></div>
    <div class="gallery__photo" role="img" aria-label="After photo of the same wall freshly painted blue-grey" style="background:linear-gradient(#b6c3d2,#6f8093)"><span class="gallery__tag" style="right:20px;top:5px">After</span></div>
    <div class="gallery__photo" role="img" aria-label="Before photo of a brick house with blue shutters" style="background:linear-gradient(#8a6a60,var(--photo-brick) 60%,#5d6a3e)"><span class="gallery__tag" style="left:6px;bottom:18px">Before</span></div>
    <div class="gallery__photo" role="img" aria-label="After photo of brick house with fresh white trim and blue shutters" style="background:linear-gradient(var(--photo-sky),#d9dde2 40%,#8b5a4d)"><span class="gallery__tag" style="right:12px;top:8px">After</span></div>
  </div>

  <div class="abs about-band"></div>
  <p class="abs about-text">Brightline Painting is a local painting contractor serving the DC metro area for over 15 years with a history of repeat customers. Our company is dedicated to providing the highest quality painting work with the best possible service that will maximize your property investment while enhancing your “living space”.</p>
  <div class="abs call-label">Make a Call</div>
  <div class="abs call-number">703-555-0148</div>

  <div class="brand">
    <span class="brand__mark"></span>
    <div class="brand__name">Brightline<br>Painting</div>
  </div>
  <div class="abs stamp-box"></div>
  <div class="abs address-line" style="top:178px"></div>
  <div class="abs address-line" style="top:221px"></div>
  <div class="abs address-line" style="top:263px"></div>
  <div class="abs address-line" style="top:306px"></div>
  <div class="abs address-line" style="top:348px"></div>
  <div class="abs address-line" style="top:390px"></div>

  <div class="abs areas-title">Painting Service Areas</div>
  <p class="abs areas-text">Falls Church, Arlington, Alexandria &amp; Old Towne, McLean, Vienna, Tysons, Fairfax County, Loudoun County, Prince William County, Washington DC, Montgomery County, Prince Georges County, Anne Arundel County, Charles County</p>

  <div class="abs contact-bar"></div>
  <div class="contact contact--addr">
    <svg width="16" height="20" viewBox="0 0 16 20"><path d="M8 0a8 8 0 0 0-8 8c0 6 8 12 8 12s8-6 8-12a8 8 0 0 0-8-8z" fill="#f6b21b"/><circle cx="8" cy="8" r="3" fill="var(--red)"/></svg>
    <span>418 MAPLE CREST ROAD, #B-12<br>FALLS CHURCH, VA 22046</span>
  </div>
  <div class="contact contact--phone">
    <svg width="22" height="16" viewBox="0 0 22 16"><path d="M2 5c0-3 18-3 18 0v2h-5V5H7v2H2z" fill="#f6b21b"/><rect x="4" y="8" width="14" height="8" rx="2" fill="#f6b21b"/></svg>
    <span>703-555-0148</span>
  </div>
  <div class="contact contact--web">
    <svg width="18" height="18" viewBox="0 0 18 18" fill="none" stroke="#f6b21b" stroke-width="1.6"><circle cx="9" cy="9" r="8"/><ellipse cx="9" cy="9" rx="3.5" ry="8"/><path d="M1 9h16M2.5 5h13M2.5 13h13"/></svg>
    <span>brightlinepainting.com<br>INFO@BRIGHTLINEPAINTING.COM</span>
  </div>
  <div class="badge" style="left:581px;width:45px"></div>
  <div class="badge" style="left:638px;width:67px"></div>
  <div class="badge" style="left:715px;width:45px"></div>

  <div class="abs footer-left"></div>
  <div class="rules" style="top:510px">
    <span style="top:0"></span><span style="top:10px"></span><span style="top:20px"></span>
  </div>
</section>

</body>
</html>
```